CORAL REFRIGERATION Business Card design

We are looking for a business card design front and back. We would like our logo only on the front with all other details on the rear.
Rear should include name, email address and two phone numbers. Similar to the attachment.
Smart and bright.
Looking for a matt finish on all of the card but the logo to be gloss and slightly proud.

Contact Information for Business Card

Name - Gavin Pellow
Director
Phone - 0893172648
0417258391
email - gavin@coralrefrigeration.com.au
website - coralrefrigeration.com.au

Font styles to use
Serif

Requirements
Must have
• Colours from our logo. icons for phone, email etc.

```html
<!DOCTYPE html>
<html lang="en">
<head>
<meta charset="utf-8">
<title>Coral Refrigeration – Business Card</title>
<link rel="stylesheet" href="https://fonts.googleapis.com/css2?family=Open+Sans:wght@400;600;700;800&display=swap">
<style>
  :root {
    --lime: #a8f56f;
    --purple: #4a2c6e;
    --ink: #1c1c1c;
    --grey: #3a3a3a;
    --paper: #ffffff;
    --backdrop: #e9eaec;
  }
  * { box-sizing: border-box; margin: 0; padding: 0; }
  html, body { width: 1200px; height: 782px; overflow: hidden; }
  body {
    background: var(--backdrop);
    font-family: "Open Sans", Arial, sans-serif;
    display: flex;
    align-items: center;
    justify-content: center;
    gap: 40px;
  }
  .card {
    position: relative;
    width: 540px;
    height: 309px;
    box-shadow: 0 6px 18px rgba(0,0,0,0.18);
    overflow: hidden;
  }
  .card-front {
    background: var(--lime);
    display: flex;
    align-items: center;
    justify-content: center;
  }
  .wordmark {
    font-weight: 800;
    color: var(--ink);
    text-align: center;
    line-height: 1.05;
    letter-spacing: 1px;
  }
  .card-front .wordmark { font-size: 40px; }
  .card-back { background: var(--paper); }
  .person { position: absolute; left: 30px; top: 26px; }
  .person-name {
    color: var(--lime);
    font-weight: 700;
    font-size: 21px;
    letter-spacing: 0.5px;
    text-transform: uppercase;
  }
  .person-role { color: var(--purple); font-size: 12px; margin-top: 1px; }
  .card-back .wordmark {
    position: absolute;
    right: 30px;
    top: 112px;
    color: var(--purple);
    font-size: 27px;
    text-align: right;
  }
  .contact-list {
    position: absolute;
    list-style: none;
    font-size: 13px;
    color: var(--grey);
    line-height: 1.45;
  }
  .contact-list li { display: flex; align-items: center; gap: 6px; }
  .contact-online { left: 30px; top: 200px; }
  .contact-phone { right: 30px; top: 222px; font-size: 15px; letter-spacing: 1px; }
  .icon { width: 12px; height: 12px; fill: var(--lime); flex: none; }
  .bands { position: absolute; left: 0; bottom: 0; width: 540px; height: 309px; }
</style>
</head>
<body>
  <section class="card card-front" aria-label="Card front">
    <p class="wordmark">CORAL<br>REFRIGERATION</p>
  </section>

  <section class="card card-back" aria-label="Card back">
    <svg class="bands" viewBox="0 0 540 309" aria-hidden="true">
      <polygon points="0,277 256,277 246,289 0,289" fill="var(--lime)"/>
      <polygon points="266,279 540,279 540,309 240,309" fill="var(--purple)"/>
    </svg>

    <div class="person">
      <p class="person-name">Gavin Pellow</p>
      <p class="person-role">Director</p>
    </div>

    <p class="wordmark">CORAL<br>REFRIGERATION</p>

    <ul class="contact-list contact-online">
      <li>
        <svg class="icon" viewBox="0 0 12 12" aria-hidden="true"><path d="M0 2h12v8H0z"/><path d="M0 2l6 4 6-4" fill="none" stroke="#fff" stroke-width="1"/></svg>
        gavin@coralrefrigeration.com.au
      </li>
      <li>
        <svg class="icon" viewBox="0 0 12 12" aria-hidden="true"><circle cx="6" cy="6" r="6"/><path d="M0 6h12M6 0c-3 3-3 9 0 12M6 0c3 3 3 9 0 12" fill="none" stroke="#fff" stroke-width="0.8"/></svg>
        coralrefrigeration.com.au
      </li>
    </ul>

    <ul class="contact-list contact-phone">
      <li>0893172648
        <svg class="icon" viewBox="0 0 12 12" aria-hidden="true"><path d="M1 4c0-2 2-3 5-3s5 1 5 3l-2 1-1-2H4L3 5zM2 6h8l1 5H1z"/></svg>
      </li>
      <li>0417258391
        <svg class="icon" viewBox="0 0 12 12" aria-hidden="true"><path d="M1 4c0-2 2-3 5-3s5 1 5 3l-2 1-1-2H4L3 5zM2 6h8l1 5H1z"/></svg>
      </li>
    </ul>
  </section>
</body>
</html>
```